Body corporate management needs business principle flyer design

We need a one page A4 flyer design for our business principles.
We manage body corporates and strata properties.
Brightwick is a new initiative for our company. Its a label that we have given to our principles of business that drive our people, systems and processes to give assurance to our clients that every detail matters.
We would like to be able to include this design in future brochure so we are after 1 x portrait and 1 x landscape.
The design needs to portray professionalism.
We would like to see designs that use the colour red. (see attached logo).

Target Market(s)

Professionals

Industry/Entity Type

Business

Font styles to use
Sans Serif

Requirements
Must have
• Brightwick logo, provide the design file and as pdf
Nice to have
• the use of the colour red from the logo

```html
<!DOCTYPE html>
<html lang="en">
<head>
<meta charset="utf-8">
<title>Brightwick – Principles of Business</title>
<link href="https://fonts.googleapis.com/css2?family=Open+Sans:wght@400;600;700&family=Syncopate:wght@400;700&display=swap" rel="stylesheet">
<style>
  :root {
    --backdrop: #5f5f5f;
    --paper: #ffffff;
    --brand-red: #b3202a;
    --band-red: #a81d26;
    --ink: #3a3a3a;
    --ink-soft: #555555;
    --tile: #dcdcdc;
    --tile-text: #8a8a8a;
    --header-grey: #dedee1;
  }
  * { box-sizing: border-box; margin: 0; padding: 0; }
  html, body { width: 1200px; height: 800px; overflow: hidden; }
  body {
    background: var(--backdrop);
    font-family: "Open Sans", Arial, sans-serif;
    color: var(--ink);
  }
  .flyer {
    position: absolute;
    left: 330px; top: 18px;
    width: 540px; height: 764px;
    background: var(--paper);
    box-shadow: 0 6px 18px rgba(0,0,0,.35);
    overflow: hidden;
  }
  .flyer-header {
    position: relative;
    height: 238px;
    background: linear-gradient(90deg, #f6f6f7 45%, var(--header-grey) 100%);
  }
  .header-photo {
    position: absolute; left: 0; top: 0;
    width: 250px; height: 238px;
    background: linear-gradient(90deg, #1f2536 0%, #2b3246 45%, #8a8e98 75%, rgba(246,246,247,0) 100%);
  }
  .touch-line {
    position: absolute; left: 0; top: 0;
    width: 540px; height: 238px;
  }
  .brand-name {
    position: absolute; left: 262px; top: 82px;
    font-size: 42px; font-weight: 400;
    color: var(--brand-red);
    letter-spacing: -0.5px;
    line-height: 1;
  }
  .tagline {
    position: absolute; left: 264px; top: 140px;
    width: 250px;
    font-size: 9.5px; line-height: 1.4;
    color: var(--ink-soft);
  }
  .principles {
    display: grid;
    grid-template-columns: 1fr 1fr;
    column-gap: 24px;
    row-gap: 10px;
    padding: 20px 28px 0 32px;
  }
  .principle { display: flex; gap: 10px; }
  .principle-number {
    flex: 0 0 26px; height: 26px;
    margin-top: 4px;
    background: var(--tile);
    color: var(--tile-text);
    font-size: 12px;
    display: flex; align-items: center; justify-content: center;
  }
  .principle-title {
    font-family: "Syncopate", Arial, sans-serif;
    font-size: 10px; font-weight: 400;
    color: var(--brand-red);
    text-transform: uppercase;
    line-height: 1.1;
    margin-bottom: 2px;
  }
  .principle-title.plain { color: var(--ink); }
  .principle-text {
    font-size: 7.6px; line-height: 1.28;
    text-align: justify;
    color: var(--ink-soft);
  }
  .principle-text strong {
    font-size: 10px; font-weight: 700;
    color: var(--ink);
  }
  .flyer-footer {
    position: absolute; left: 0; bottom: 0;
    width: 100%; height: 12px;
    background: var(--band-red);
  }
</style>
</head>
<body>
  <main class="flyer">
    <header class="flyer-header">
      <div class="header-photo" role="img" aria-label="Businessman in a dark suit reaching out to touch a glowing point on a virtual screen"></div>
      <svg class="touch-line" viewBox="0 0 540 238" aria-hidden="true">
        <circle cx="186" cy="72" r="10" fill="none" stroke="#c8434b" stroke-width="1"/>
        <circle cx="186" cy="72" r="5" fill="#c8343d"/>
        <line x1="196" y1="74" x2="262" y2="112" stroke="#c8434b" stroke-width="0.8"/>
      </svg>
      <h1 class="brand-name">Brightwick</h1>
      <p class="tagline">Brightwick is our principles of business that drive our people, systems and processes to give assurance to our clients that every detail matters.</p>
    </header>

    <section class="principles">
      <article class="principle">
        <div class="principle-number">1</div>
        <div>
          <h2 class="principle-title">Client Experience</h2>
          <p class="principle-text"><strong>Our promise is</strong> to pursue excellence and to continually deliver a solutions based service. We achieve this through active engagement, open channels of communication and a serviced led team with the dedicated resources to listen, engage and implement.</p>
        </div>
      </article>
      <article class="principle">
        <div class="principle-number">2</div>
        <div>
          <h2 class="principle-title">Loyalty</h2>
          <p class="principle-text"><strong>We seek to develop</strong> a life-time relationship with our clients, building trust by acting with integrity, honesty and courtesy. We achieve this due to our expert approach to strata management and providing a responsive service to our clients.</p>
        </div>
      </article>
      <article class="principle">
        <div class="principle-number">3</div>
        <div>
          <h2 class="principle-title">Education and Guidance</h2>
          <p class="principle-text"><strong>We endeavor</strong> to always be proactive in client education and guidance. This is achieved by our internal and external communications, comprehensive training programs and cross-departmental collaboration of knowledge sharing, dedicated resources to listen, engage and implement.</p>
        </div>
      </article>
      <article class="principle">
        <div class="principle-number">4</div>
        <div>
          <h2 class="principle-title">Compliance and Governance</h2>
          <p class="principle-text"><strong>We strive to be the best</strong> in our field, by implementing efficiencies without compromising service quality, accuracy or compliance. We continually seek to achieve this by reviewing, updating and adopting continuous improvement strategies, systems and quality processes that deliver outcomes.</p>
        </div>
      </article>
      <article class="principle">
        <div class="principle-number">5</div>
        <div>
          <h2 class="principle-title plain">Systems and Processes</h2>
          <p class="principle-text"><strong>We strive to be the best</strong> in our field, by implementing efficiencies without compromising service quality, accuracy or compliance. We continually seek to achieve this by reviewing, updating and adopting continuous improvement strategies, systems and quality processes that deliver outcomes.</p>
        </div>
      </article>
      <article class="principle">
        <div class="principle-number">6</div>
        <div>
          <h2 class="principle-title">Quality and Commitment</h2>
          <p class="principle-text"><strong>We invest</strong> in the recruitment and retention of a quality and diverse team of experienced professionals with a strong focus on continual professional development. As committed and skilled individuals, we actively promote the cross-departmental collaboration with one another to deliver a well rounded offering.</p>
        </div>
      </article>
      <article class="principle">
        <div class="principle-number">7</div>
        <div>
          <h2 class="principle-title">Delivery</h2>
          <p class="principle-text"><strong>We empower</strong> our teams to deliver an outstanding client service and to be accountable for their actions. We will make sure every detail matters, provide valuable insight and supply information in a clear and timely manner.</p>
        </div>
      </article>
      <article class="principle">
        <div class="principle-number">8</div>
        <div>
          <h2 class="principle-title">Integrity</h2>
          <p class="principle-text"><strong>Our approach</strong> to strata management is bound by honesty and a strong set of moral principles. We act in our clients' best interests with diligence and transparency for understanding and accountability.</p>
        </div>
      </article>
      <article class="principle">
        <div class="principle-number">9</div>
        <div>
          <h2 class="principle-title">Continuous Improvement</h2>
          <p class="principle-text"><strong>Our goal is</strong> to continually evolve to better our offering and to be adaptable and responsive to change. Our infrastructure supports us to continually mould into the business that is right for our clients.</p>
        </div>
      </article>
      <article class="principle">
        <div class="principle-number">10</div>
        <div>
          <h2 class="principle-title">Ethical Stance</h2>
          <p class="principle-text"><strong>We aim to create</strong> a community of ethical business relationships where we contribute our values and services to give our clients outstanding reassurance of our abilities.</p>
        </div>
      </article>
    </section>

    <footer class="flyer-footer"></footer>
  </main>
</body>
</html>
```